Web Design Project for Web Agency

WHAT I NEED:
The design I need (PSD file) is for a microsite designed for employee recruitment for Brantley, a Web agency.
***Design for the 1st Page ONLY : "Manifeste"
OBJECTIVES OF THE WEBSITE:
1. To promote the agency's corporate culture and HR management principles.
2. To get people to apply on available jobs
ELEMENTS OF THE PAGE "MANIFESTE" :
1. Brantley logo (see attached files). Beside the logo must be the word "Carrières" ("Careers" in english)
***The logo is not final and there is NO branding for Brantley yet. That is why there are multiple files. So please feel free to be creative!
2. Main menu : 4 sections
Manifeste | Opportunités | Brantly | Postuler
3. Manifeste :
This page is the home page. It will present 2 main sections :
a. The agency's corporate culture :
- Title of the page is a question : "Do you embrace Brantley's corporate culture?"
- Then, presentation of the 5 corporate values, each with a title and short description
- At the end of the list of values, we want a button that says "Apply now"
b. The agency's HR management principles :
- Title of the page is a question : "Do you see yourself working at Brantley?"
- Then, presentation of the 5 Management principles, each with a title and short description
- At the end of the list of principles, we want a button that says "Apply now"
VISUAL INSPIRATION
To create each section of the "Manifeste" page, we want a design that will fit with the corporate culture:
- Brantley is BOLD
- Brantley is PROUD
- Brantley is PROFESSIONAL
- Brantley is ELEGANT
- Brantley is REFINED
We want something slick and modern. Here are some Website's that we like that can be of inspiration:
- http://www.studio-vetrak.com/en/services
- http://quorvinpanels.com/

```html
<!DOCTYPE html>
<html lang="fr">
<head>
<meta charset="utf-8">
<title>Brantley – Carrières – Manifeste</title>
<link rel="stylesheet" href="https://fonts.googleapis.com/css2?family=Josefin+Sans:wght@300;400&family=Montserrat:wght@700&family=Questrial&family=Arimo:wght@400;700&display=swap">
<style>
  :root {
    --orange: #f26b2a;
    --orange-light: #f08a5a;
    --cyan: #16c3e0;
    --cyan-dark: #0aa8c4;
    --ink: #111111;
    --paper: #f4f3f2;
    --hex-grey: #ececeb;
    --hex-line: #dcdcdc;
    --text-grey: #9a9a9a;
    --footer-band: #e9e9e9;
    --white: #ffffff;
  }
  * { box-sizing: border-box; margin: 0; padding: 0; }
  html, body { width: 961px; height: 1200px; overflow: hidden; }
  body {
    position: relative;
    background: var(--paper);
    font-family: "Arimo", Arial, sans-serif;
    color: var(--ink);
  }
  .abs { position: absolute; }

  .hero-band { position: absolute; left: 0; top: 0; width: 961px; height: 523px; }

  .topbar { position: absolute; left: 0; top: 0; width: 961px; height: 34px; }
  .main-nav {
    position: absolute; top: 10px; left: 475px;
    display: flex; gap: 21px;
    font-size: 11px; color: var(--white);
  }
  .social {
    position: absolute; top: 11px; left: 780px;
    display: flex; gap: 12px;
  }
  .social span { width: 12px; height: 12px; border-radius: 50%; background: var(--white); display: block; }

  .brand { position: absolute; left: 98px; top: 60px; text-align: center; }
  .brand-name {
    font-family: "Questrial", sans-serif;
    font-size: 35px; color: var(--orange); letter-spacing: 0.5px; line-height: 1;
  }
  .brand-tag {
    font-family: "Questrial", sans-serif;
    font-size: 8px; letter-spacing: 3.4px; color: #777; margin-top: 8px;
  }
  .careers {
    position: absolute; left: 123px; top: 160px;
    font-family: "Questrial", sans-serif; font-size: 14px;
    display: flex; align-items: center; gap: 12px;
  }
  .careers .arrow-box { width: 19px; height: 11px; background: var(--ink); display: flex; align-items: center; justify-content: center; }

  .hero-copy {
    position: absolute; left: 302px; top: 162px; width: 500px;
    text-align: center; color: var(--white);
    font-family: "Josefin Sans", sans-serif; font-weight: 400;
    font-size: 22px; line-height: 40px; letter-spacing: 0.5px;
  }
  .hero-copy strong { font-family: "Montserrat", sans-serif; font-weight: 700; font-size: 20px; }

  .btn {
    position: absolute; display: flex; align-items: center; justify-content: center;
    color: var(--white); font-weight: 700; letter-spacing: 0.6px;
    border-radius: 5px;
  }
  .btn-cyan { background: linear-gradient(var(--cyan), var(--cyan-dark)); box-shadow: 0 2px 0 #0a8ea6; }
  .btn-orange { background: linear-gradient(var(--orange-light), #ec7440); box-shadow: 0 0 0 4px #f7e2d6; }
  .btn-cyan.framed { box-shadow: 0 0 0 4px #d7f2f7; }
  .hero-btn { left: 453px; top: 285px; width: 190px; height: 32px; font-size: 13px; }

  .section-title {
    position: absolute; left: 0; width: 961px; text-align: center;
    font-family: "Josefin Sans", sans-serif; font-weight: 300;
    font-size: 25px; letter-spacing: 0.3px;
  }
  .section-title b { font-weight: 400; }
  .title-culture { top: 480px; color: var(--orange); }
  .title-work { top: 803px; color: var(--cyan); }

  .values { position: absolute; left: 0; width: 961px; height: 110px; }
  .value-label { font-family: "Arimo", sans-serif; font-size: 10px; }

  .value-desc {
    position: absolute; left: 380px; width: 200px; text-align: center;
    font-size: 9.5px; line-height: 11px; color: var(--text-grey);
  }

  .to-top {
    position: absolute; left: 780px; top: 1079px; width: 63px; height: 33px;
    background: var(--ink); border-radius: 32px 32px 0 0;
    display: flex; justify-content: center; padding-top: 12px;
  }

  .footer-links {
    position: absolute; left: 0; top: 1112px; width: 961px; height: 44px;
    background: var(--footer-band);
    display: flex; justify-content: center; align-items: center; gap: 6px;
    font-size: 9.5px; color: #222;
  }
  .footer-bottom { position: absolute; left: 0; top: 1156px; width: 961px; height: 44px; }
  .copyright { position: absolute; left: 98px; top: 1173px; font-size: 9.5px; color: var(--white); }
  .footer-brand { position: absolute; left: 762px; top: 1161px; text-align: center; }
  .footer-brand .name { font-family: "Questrial", sans-serif; font-size: 22px; color: var(--ink); line-height: 1; font-weight: 400; }
  .footer-brand .tag { font-family: "Questrial", sans-serif; font-size: 7px; letter-spacing: 2px; color: #444; margin-top: 4px; }
</style>
</head>
<body>

  <svg class="hero-band" viewBox="0 0 961 523" role="img" aria-label="Orange band with light rays and silhouettes of business people at work">
    <defs>
      <radialGradient id="heroGlow" cx="0.6" cy="0.3" r="0.7">
        <stop offset="0" stop-color="#f47a35"/>
        <stop offset="1" stop-color="#ef6424"/>
      </radialGradient>
    </defs>
    <polygon points="432,0 961,0 961,229 0,523 0,429" fill="url(#heroGlow)"/>
  </svg>

  <svg class="topbar" viewBox="0 0 961 34" aria-hidden="true">
    <polygon points="395,34 429,0 961,0 961,34" fill="#000"/>
  </svg>
  <nav class="main-nav">
    <span>Manifeste</span><span>Opportunités</span><span>Brantly</span><span>Postuler</span>
  </nav>
  <div class="social" aria-label="Réseaux sociaux">
    <span></span><span></span><span></span><span></span>
  </div>

  <div class="brand">
    <div class="brand-name">Brantley</div>
    <div class="brand-tag">AGENCE NUMÉRIQUE</div>
  </div>
  <div class="careers">Carrières
    <span class="arrow-box">
      <svg width="11" height="7" viewBox="0 0 11 7"><path d="M0 3.5H9M6 0.5L9.5 3.5L6 6.5" stroke="#fff" stroke-width="1.6" fill="none"/></svg>
    </span>
  </div>

  <div class="hero-copy">
    <div><strong>BRANTLEY</strong> SEM NON AUGUE POSUERE,</div>
    <div><strong>PHARETRA</strong> SUSCIPIT URNA MATTIS.</div>
    <div>ANTE <strong>IPSUM PRIMIS</strong></div>
  </div>
  <div class="btn btn-cyan hero-btn">APPLY NOW!</div>

  <h2 class="section-title title-culture">DO YOU EMBRACE BRANTLEY'S CORPORATE CULTURE<b>?</b></h2>

  <svg class="values" style="top:546px" viewBox="0 0 961 110" aria-label="Valeurs de l'agence">
    <g fill="#e2e2e1" opacity="0.7">
      <ellipse cx="157" cy="116" rx="32" ry="8"/><ellipse cx="307" cy="116" rx="32" ry="8"/>
      <ellipse cx="637" cy="116" rx="32" ry="8"/><ellipse cx="794" cy="116" rx="32" ry="8"/>
    </g>
    <g stroke="#dedede" fill="#efefee">
      <polygon points="157,4 201,28 201,76 157,100 113,76 113,28"/>
      <polygon points="307,4 351,28 351,76 307,100 263,76 263,28"/>
      <polygon points="637,4 681,28 681,76 637,100 593,76 593,28"/>
      <polygon points="794,4 838,28 838,76 794,100 750,76 750,28"/>
    </g>
    <polygon points="473,4 517,28 517,76 473,100 429,76 429,28" fill="#16b9d6" stroke="#222" stroke-width="1"/>
    <g fill="#d9d9d9">
      <path d="M146 48 L166 30 L170 34 L150 52 L144 54 Z"/>
      <rect x="295" y="38" width="16" height="15" rx="2"/><rect x="311" y="41" width="6" height="8" rx="3" fill="none" stroke="#d9d9d9" stroke-width="2"/>
      <circle cx="630" cy="33" r="3"/><circle cx="644" cy="33" r="3"/><rect x="626" y="38" width="8" height="14" rx="2"/><rect x="640" y="38" width="8" height="14" rx="2"/>
      <path d="M780 44 L810 30 L800 52 L794 44 Z"/>
    </g>
    <g fill="#fff">
      <rect x="465" y="24" width="16" height="14" rx="4"/><rect x="462" y="38" width="22" height="4" rx="2"/>
      <rect x="472" y="42" width="2" height="6"/><path d="M463 52 L473 47 L483 52" stroke="#fff" stroke-width="2" fill="none"/>
    </g>
    <g class="value-label" text-anchor="middle" fill="#a8a8a8">
      <text x="157" y="74">Consectetur</text><text x="307" y="74">Consectetur</text>
      <text x="473" y="74" fill="#fff">Consectetur</text>
      <text x="637" y="74">Consectetur</text><text x="794" y="74">Consectetur</text>
    </g>
  </svg>
  <p class="value-desc" style="top:685px">Lorem ipsum dolor sit<br>adipiscing elit. Ut vulputate</p>
  <div class="btn btn-orange" style="left:385px;top:719px;width:190px;height:31px;font-size:14px">APPLY NOW!</div>

  <h2 class="section-title title-work">DO YOU SEE YOURSELF WORKING AT BRANTLEY<b>?</b></h2>

  <svg class="values" style="top:869px" viewBox="0 0 961 110" aria-label="Principes de gestion">
    <g fill="#e2e2e1" opacity="0.7">
      <ellipse cx="157" cy="116" rx="32" ry="8"/><ellipse cx="307" cy="116" rx="32" ry="8"/>
      <ellipse cx="637" cy="116" rx="32" ry="8"/><ellipse cx="794" cy="116" rx="32" ry="8"/>
    </g>
    <g stroke="#dedede" fill="#efefee">
      <polygon points="157,4 201,28 201,76 157,100 113,76 113,28"/>
      <polygon points="307,4 351,28 351,76 307,100 263,76 263,28"/>
      <polygon points="637,4 681,28 681,76 637,100 593,76 593,28"/>
      <polygon points="794,4 838,28 838,76 794,100 750,76 750,28"/>
    </g>
    <polygon points="473,4 517,28 517,76 473,100 429,76 429,28" fill="#f26b2a" stroke="#222" stroke-width="1"/>
    <g fill="#d9d9d9">
      <path d="M146 48 L166 30 L170 34 L150 52 L144 54 Z"/>
      <rect x="295" y="38" width="16" height="15" rx="2"/><rect x="311" y="41" width="6" height="8" rx="3" fill="none" stroke="#d9d9d9" stroke-width="2"/>
      <circle cx="630" cy="33" r="3"/><circle cx="644" cy="33" r="3"/><rect x="626" y="38" width="8" height="14" rx="2"/><rect x="640" y="38" width="8" height="14" rx="2"/>
      <path d="M780 44 L810 30 L800 52 L794 44 Z"/>
    </g>
    <g fill="#fff">
      <rect x="465" y="24" width="16" height="14" rx="4"/><rect x="462" y="38" width="22" height="4" rx="2"/>
      <rect x="472" y="42" width="2" height="6"/><path d="M463 52 L473 47 L483 52" stroke="#fff" stroke-width="2" fill="none"/>
    </g>
    <g class="value-label" text-anchor="middle" fill="#a8a8a8">
      <text x="157" y="74">Consectetur</text><text x="307" y="74">Consectetur</text>
      <text x="473" y="74" fill="#fff">Consectetur</text>
      <text x="637" y="74">Consectetur</text><text x="794" y="74">Consectetur</text>
    </g>
  </svg>
  <p class="value-desc" style="top:1008px">Lorem ipsum dolor sit<br>adipiscing elit. Ut vulputate</p>
  <div class="btn btn-cyan framed" style="left:385px;top:1044px;width:190px;height:31px;font-size:14px">APPLY NOW!</div>

  <div class="to-top" aria-label="Retour en haut">
    <svg width="9" height="9" viewBox="0 0 9 9"><path d="M4.5 9V1M1 4.5L4.5 1L8 4.5" stroke="#fff" stroke-width="1.6" fill="none"/></svg>
  </div>

  <nav class="footer-links">
    <span>Manifeste</span><span>|</span><span>Opportunités</span><span>|</span><span>Brantly</span><span>|</span><span>Postuler</span>
  </nav>

  <svg class="footer-bottom" viewBox="0 0 961 44" aria-hidden="true">
    <rect width="961" height="44" fill="#f4f3f2"/>
    <polygon points="0,0 540,0 576,44 0,44" fill="#000"/>
  </svg>
  <p class="copyright">Copyright © Brantley Agence Numerique</p>
  <div class="footer-brand">
    <div class="name">Brantley</div>
    <div class="tag">agence numérique</div>
  </div>

</body>
</html>
```